●A4サイズ1ページにつき、横5列・縦6列で商品を配置し、各商品名、品番、画像、コピー、税込価格を入れてください
(商品の詳細説明やカラー、サイズなどはネットショップを見てもらうので記載不要です)

●定期的に商品の入れ替えを行うので、各商品の入れ替えがしやすいレイアウト、デザインにしてください

●商品はジャンルごとにまとめて掲載するので、その場所が何のジャンルかわかるようにしてください

●コンペで制作いただく1ページ目の商品・ジャンルと参考URLは添付ファイルをご覧ください

●ショップリニューアルを予定しており、リニューアル後のショップイメージで作成をお願いします

●1ページ目の上2段分のスペースに下記内容を入れてください
・ショップロゴ(添付ファイル:リニューアル前後で入れ替えできるようにしてください)
・注文方法(ショップURL(トップ画面右上の「search」で品番か商品名を検索)、2次元バーコード、「トルミナショップ」で検索、TEL、FAX)
・当日出荷について
・交換返品サービスについて
・送料無料クーポン(商品到着から30日以内、商品到着日記入欄、クーポンコード(K3928P)、使用方法(ご連絡欄記入、電話の場合は口頭))
A4
4ページ
重視する点・検討基準
・厳選した商品を取り扱っている信頼感と親しみやすさを感じさせるイメージ・デザイン
・各商品の特長が一目でわかり、興味を持ってもらえるような画像、コピー、デザイン
・送料無料クーポンが一目でわかり、期限内に注文しないと損をしてしまうと感じさせる見せ方
・他ショップでは行っていないサイズ交換・返品1年保証サービスの価値が伝わる見せ方

納品形式
Illustrator(CS4以下)またはPhotoshop(CS4以下)、及び確認用の高解像度JPGでお願いします。
アウトライン済/未アウトラインデータの両方お願いします。
使用されているフォントと制作環境もお知らせください。
印刷会社でそのまま印刷できるものを納品ください。
参考URLに誤りがありました。

http://tolmina-shop.com/tolmina/7.1/141/

http://tolmina-shop.com/tolmina/7.1/911/

よろしくお願いいたします。
報酬について説明不足だったかもしれません。
今回の金額は依頼内容である全4ページ分の報酬金額です。
1ページ分と伝わってしまった方には申し訳ありません。
紙面で使用する画像・文章は主にこちらを参考にしてください。
http://tolminashop.com/ranking/
これだけで不十分と思われる商品がありましたら、各商品ページから画像・文章を取ってきてください。

予想以上に作業の手間がかかるという声をいただきましたので、依頼金額を増額し、締め切りを延長させていただきました。

デザイン・レイアウトがわかりやすく、商品説明もポイントを捉えて入れていただいたご提案を選ばせていただきました。

商品点数が多く手間がかかったと思いますが、良いご提案をいただきありがとうございました。

```html
<!DOCTYPE html>
<html lang="ja">
<head>
<meta charset="utf-8">
<title>すこやかなかま カタログ</title>
<link href="https://fonts.googleapis.com/css2?family=M+PLUS+Rounded+1c:wght@700;800&family=Noto+Sans+JP:wght@400;700;900&display=swap" rel="stylesheet">
<style>
:root{
  --pink:#e8548a;
  --pink-light:#fbe3ec;
  --red:#e3141c;
  --blue:#3f86c8;
  --blue-light:#e3eef8;
  --ink:#333;
  --gray:#777;
  --line:#d9d9d9;
  --paper:#fff;
}
*{margin:0;padding:0;box-sizing:border-box}
html,body{width:849px;height:1200px;overflow:hidden;background:var(--paper)}
body{font-family:"Noto Sans JP",sans-serif;color:var(--ink);position:relative}
.page{width:849px;height:1200px;position:relative}

/* header */
.header{position:absolute;left:0;top:0;width:849px;height:275px}
.order{position:absolute;left:12px;top:6px;width:405px}
.brand{display:flex;align-items:center;gap:8px}
.brand-mark{width:30px;height:30px;border-radius:50%;background:var(--pink)}
.brand-name{font-family:"M PLUS Rounded 1c",sans-serif;font-weight:800;font-size:38px;color:var(--pink);letter-spacing:1px;line-height:1.2}
.tagline{font-size:12px;color:var(--gray);margin:0 0 0 40px}
.order-title{margin-top:6px;background:var(--pink);color:#fff;font-weight:700;font-size:13px;padding:2px 10px;width:130px;border-radius:2px}
.url{font-size:18px;font-weight:900;color:var(--pink);margin-top:4px;line-height:1.3}
.order-row{display:flex;gap:10px;align-items:flex-start}
.order-left{flex:1}
.order-note{font-size:11px;margin-top:2px}
.search{display:flex;margin-top:4px;width:230px;height:22px;border:2px solid var(--pink);border-radius:3px}
.search span{flex:1;font-size:11px;color:#aaa;padding:2px 6px;line-height:16px}
.search i{width:26px;background:var(--pink)}
.qr{width:58px;height:58px;border:2px solid var(--ink);background:#eee;margin-top:2px}
.contact{font-size:11px;margin-top:6px}
.tel{font-size:18px;font-weight:900;color:var(--pink);line-height:1.2}
.tel small{font-size:10px;font-weight:400;color:var(--ink)}
.ship-bar{position:absolute;left:0;top:254px;width:849px;height:19px;background:var(--pink-light);font-size:11px;font-weight:700;color:var(--red);padding:1px 12px}

.coupon{position:absolute;left:425px;top:6px;width:414px;height:140px;border:3px dashed var(--red);border-radius:4px;background:#fff}
.coupon-head{background:var(--red);color:#fff;font-weight:900;font-size:22px;text-align:center;height:38px;line-height:38px}
.coupon-body{display:flex;padding:6px 10px;gap:10px}
.coupon-code{flex:1;text-align:center;border-right:1px solid var(--line)}
.coupon-code small{display:block;font-size:11px}
.coupon-code b{font-size:28px;color:var(--red);letter-spacing:2px}
.coupon-date{flex:1.3;font-size:12px}
.date-field{display:flex;gap:4px;margin:4px 0}
.date-field span{border-bottom:1px solid var(--ink);width:34px;height:20px;text-align:right;font-size:11px}
.limit{background:var(--red);color:#fff;font-weight:900;font-size:12px;padding:2px 6px;display:inline-block}
.coupon-note{position:absolute;left:425px;top:150px;width:414px;font-size:10px;line-height:1.4}

.guarantee{position:absolute;left:425px;top:182px;width:414px;height:66px;display:flex;align-items:center;gap:8px}
.try{border:2px solid var(--pink);color:var(--pink);font-weight:900;font-size:13px;line-height:1.25;padding:4px 6px;text-align:center}
.year{background:var(--pink);color:#fff;font-weight:900;font-size:20px;padding:8px 10px;border-radius:4px;white-space:nowrap}
.swap{width:58px;height:58px;flex:none;border-radius:50%;background:var(--blue);color:#fff;font-size:10px;font-weight:700;display:flex;align-items:center;justify-content:center;text-align:center;line-height:1.2}
.guarantee p{flex:1;font-size:10px;line-height:1.4}

/* genres */
.genre{position:absolute;left:0;width:849px;border-top:3px solid var(--genre)}
.genre-new{top:275px;height:370px;--genre:var(--pink)}
.genre-back{top:645px;height:555px;--genre:var(--blue)}
.genre-label{position:absolute;left:0;top:0;bottom:0;width:22px;background:var(--genre);color:#fff;font-weight:900;font-size:15px;writing-mode:vertical-rl;text-align:center;padding-top:20px;letter-spacing:4px}
.grid{position:absolute;left:24px;right:0;top:0;bottom:0;display:grid;grid-template-columns:repeat(5,1fr);grid-auto-rows:1fr}
.item{border-right:1px dotted var(--line);border-bottom:1px dotted var(--line);padding:4px 5px 3px;display:flex;flex-direction:column;min-height:0}
.copy{font-size:9px;line-height:1.3;color:var(--genre);font-weight:700;height:24px;overflow:hidden}
.photo{flex:1;min-height:0;border-radius:3px;margin:2px 0;background:linear-gradient(160deg,#f4ede6,#d9cabb)}
.photo.cool{background:linear-gradient(160deg,#eef1f4,#b9c4cf)}
.photo.warm{background:linear-gradient(160deg,#fbe9e1,#e7b9a6)}
.photo.dark{background:linear-gradient(160deg,#e6e1dc,#8f857c)}
.name{font-size:10px;font-weight:700;line-height:1.3;height:16px;white-space:nowrap;overflow:hidden}
.meta{display:flex;align-items:baseline;gap:4px;line-height:1.2}
.code{background:var(--genre);color:#fff;font-size:11px;font-weight:700;padding:0 4px;border-radius:2px}
.price{color:var(--red);font-weight:900;font-size:19px;letter-spacing:-.5px}
.price small{font-size:11px}
</style>
</head>
<body>
<div class="page">
  <header class="header">
    <section class="order">
      <div class="brand"><span class="brand-mark"></span><span class="brand-name">すこやかなかま</span></div>
      <p class="tagline">〜 美は健康なり、健康は美なり 〜</p>
      <p class="order-title">ご注文方法</p>
      <p class="url">http://www.sukoyaka-nakama.jp/</p>
      <div class="order-row">
        <div class="order-left">
          <div class="search"><span>品番キーワード</span><i></i></div>
          <p class="order-note">品番または商品名を入力して検索</p>
        </div>
        <div class="qr" role="img" aria-label="ショップページへの2次元コード"></div>
      </div>
      <p class="contact">電話・FAXでもご注文できます</p>
      <p class="tel">TEL 048-000-3141 <small>(平日10時〜18時)</small></p>
      <p class="tel">FAX 048-000-5926 <small>(24時間受付)</small></p>
    </section>

    <section class="coupon">
      <div class="coupon-head">送料無料クーポン</div>
      <div class="coupon-body">
        <div class="coupon-code"><small>クーポンコード</small><b>K3928P</b></div>
        <div class="coupon-date">
          商品到着日
          <div class="date-field"><span>年</span><span>月</span><span>日</span></div>
          <span class="limit">商品到着から30日以内有効</span>
        </div>
      </div>
    </section>
    <p class="coupon-note">ご注文の際にご連絡欄へクーポンコードをご記入ください。お電話の場合はオペレーターにお伝えください。</p>

    <section class="guarantee">
      <div class="try">しっかり試して<br>みてください</div>
      <div class="year">1年間保証</div>
      <div class="swap">サイズ交換<br>・返品</div>
      <p>商品の使用後でも「サイズが合わない」「効果が感じられない」場合は到着から1年間、交換・返品を承ります。</p>
    </section>
    <p class="ship-bar">●平日14時・土曜10時までのご注文は当日出荷いたします。(お休みの日を除く)</p>
  </header>

  <section class="genre genre-new">
    <h2 class="genre-label">新商品</h2>
    <div class="grid">
      <article class="item"><p class="copy">背中をほぐす<br>寝るだけストレッチ</p><div class="photo" role="img" aria-label="背中ストレッチまくらの商品写真"></div><p class="name">のびのび背中まくら</p><p class="meta"><span class="code">541</span><span class="price">3,780<small>円</small></span></p></article>
      <article class="item"><p class="copy">履くだけで<br>ふくらはぎすっきり</p><div class="photo cool" role="img" aria-label="着圧ソックスの商品写真"></div><p class="name">らくらく着圧ソックス</p><p class="meta"><span class="code">545</span><span class="price">2,376<small>円</small></span></p></article>
      <article class="item"><p class="copy">足指を広げて<br>正しい姿勢に</p><div class="photo warm" role="img" aria-label="足指サポーターの商品写真"></div><p class="name">ゆびひろげサポーター</p><p class="meta"><span class="code">543</span><span class="price">2,052<small>円</small></span></p></article>
      <article class="item"><p class="copy">足元ぽかぽか<br>朝までぐっすり</p><div class="photo dark" role="img" aria-label="就寝用ソックスの商品写真"></div><p class="name">ぬくもり就寝ソックス</p><p class="meta"><span class="code">550</span><span class="price">1,728<small>円</small></span></p></article>
      <article class="item"><p class="copy">歩くたびに<br>美しい脚へ</p><div class="photo" role="img" aria-label="サンダルの商品写真"></div><p class="name">すらり美脚サンダル</p><p class="meta"><span class="code">547</span><span class="price">8,023<small>円</small></span></p></article>

      <article class="item"><p class="copy">座るだけで<br>おしりほかほか</p><div class="photo warm" role="img" aria-label="座布団の商品写真"></div><p class="name">ぽかぽか座布団</p><p class="meta"><span class="code">559</span><span class="price">1,981<small>円</small></span></p></article>
      <article class="item"><p class="copy">はさむだけで<br>ふくらはぎケア</p><div class="photo cool" role="img" aria-label="ふくらはぎケア器具の商品写真"></div><p class="name">ふくらはぎ挟みケア</p><p class="meta"><span class="code">560</span><span class="price">3,480<small>円</small></span></p></article>
      <article class="item"><p class="copy">ふわふわの<br>履き心地</p><div class="photo" role="img" aria-label="室内サンダルの商品写真"></div><p class="name">ふんわり室内サンダル</p><p class="meta"><span class="code">564</span><span class="price">6,980<small>円</small></span></p></article>
      <article class="item"><p class="copy">骨盤まわりを<br>ゆらしてほぐす</p><div class="photo dark" role="img" aria-label="骨盤ボードの商品写真"></div><p class="name">ゆらゆら骨盤ボード</p><p class="meta"><span class="code">558</span><span class="price">9,155<small>円</small></span></p></article>
      <article class="item"><p class="copy">肌にやさしい<br>天然素材</p><div class="photo cool" role="img" aria-label="パジャマの商品写真"></div><p class="name">ふわり綿パジャマ</p><p class="meta"><span class="code">566</span><span class="price">14,580<small>円</small></span></p></article>
    </div>
  </section>

  <section class="genre genre-back">
    <h2 class="genre-label">腰痛</h2>
    <div class="grid">
      <article class="item"><p class="copy">腰への負担を<br>やわらげる円座</p><div class="photo" role="img" aria-label="円座クッションの商品写真"></div><p class="name">ドーナツ型クッション</p><p class="meta"><span class="code">911</span><span class="price">5,400<small>円</small></span></p></article>
      <article class="item"><p class="copy">ぶら下がるだけで<br>腰すっきり</p><div class="photo cool" role="img" aria-label="ストレッチ器具の商品写真"></div><p class="name">ゆらし腰ストレッチ</p><p class="meta"><span class="code">235</span><span class="price">7,179<small>円</small></span></p></article>
      <article class="item"><p class="copy">姿勢を支える<br>背筋サポート</p><div class="photo warm" role="img" aria-label="姿勢ベルトの商品写真"></div><p class="name">しゃんと姿勢ベルト</p><p class="meta"><span class="code">436</span><span class="price">5,076<small>円</small></span></p></article>
      <article class="item"><p class="copy">巻くだけで<br>腰をしっかり支える</p><div class="photo dark" role="img" aria-label="腰ベルトの商品写真"></div><p class="name">しっかり腰ベルトDX</p><p class="meta"><span class="code">917</span><span class="price">10,080<small>円</small></span></p></article>
      <article class="item"><p class="copy">ハイテク素材で<br>腰をあたためる</p><div class="photo" role="img" aria-label="腰用サポーターの商品写真"></div><p class="name">あたため腰サポーター</p><p class="meta"><span class="code">223</span><span class="price">9,720<small>円</small></span></p></article>

      <article class="item"><p class="copy">巻いて温める<br>シリコン製</p><div class="photo cool" role="img" aria-label="骨盤ベルトの商品写真"></div><p class="name">やわらか骨盤ベルト</p><p class="meta"><span class="code">237</span><span class="price">6,372<small>円</small></span></p></article>
      <article class="item"><p class="copy">寝ながら全身を<br>やさしく伸ばす</p><div class="photo dark" role="img" aria-label="ストレッチ台の商品写真"></div><p class="name">寝たままストレッチ台</p><p class="meta"><span class="code">237</span><span class="price">30,651<small>円</small></span></p></article>
      <article class="item"><p class="copy">腰にやさしい<br>座り心地</p><div class="photo warm" role="img" aria-label="座椅子の商品写真"></div><p class="name">ゆったり腰楽座椅子</p><p class="meta"><span class="code">500</span><span class="price">36,000<small>円</small></span></p></article>
      <article class="item"><p class="copy">揺らすだけで<br>骨盤ほぐし</p><div class="photo" role="img" aria-label="骨盤枕の商品写真"></div><p class="name">ころころ骨盤枕</p><p class="meta"><span class="code">558</span><span class="price">9,155<small>円</small></span></p></article>
      <article class="item"><p class="copy">極上の寝心地で<br>腰を守る</p><div class="photo cool" role="img" aria-label="マットレスの商品写真"></div><p class="name">ぐっすり体圧マットレス</p><p class="meta"><span class="code">233</span><span class="price">14,580<small>円</small></span></p></article>
    </div>
  </section>
</div>
</body>
</html>
```